UK garage/funky house night flier

I need a flier design to upload to my sociallink event page and also some printed fliers to promote the event.

Event is in an urban area underneath railway arches so would like a flier to reflect this with an urban background.

new photos uploaded to be used as possible backgrounds

Target Market(s)

aged 18-30

Industry/Entity Type

House

Requirements
Must have
• The following text on front of flier:

TRUE PULSE ENTERTAINMENTS PRESENTS A NIGHT CALLED…

‘MIDNIGHT CELLAR RHYTHMZ’

Saturday 7th September 2013

@ Dock47, Harlow Lane, Digbeth, Birmingham B9 3QW

9pm till late

DJ’s playing a selection of Funky house/deep house/future garage and old school 2-step garage

(On back of flier......)

Come and enjoy yourself in a friendly, safe environment with like-minded people who are out to have a good time and rave till the early hours. This venue is part outdoor terrace and part indoor with music being played on the Wavecraft Soundsystem – so you know it is a night not to be missed!!

This event is guestlist only. Those not on the guest list will not be allowed entry. To get yourself on the guest list go to the sociallink page www.sociallink.example/truepulseentertainments and join the event ‘Midnight Cellar Rhythmz’

Dresscode: smart. No trainers/tracksuits
Admission fee on the door is £5
Last entry: midnight
Nice to have
• must be portrait, A5 or A6 size

Urban background, maybe at night, a street with old brickwork, maybe some speakers in the foreground.

dock47 logo bottom right

Back of flier to have the map of Dock47

```html
<!DOCTYPE html>
<html lang="en">
<head>
<meta charset="utf-8">
<title>Midnight Cellar Rhythmz – Flier</title>
<link href="https://fonts.googleapis.com/css2?family=Architects+Daughter&family=Patrick+Hand&display=swap" rel="stylesheet">
<style>
  :root {
    --page-bg: #ffffff;
    --paper: #eef0f0;
    --paper-light: #f6f7f7;
    --grunge: #8e9192;
    --ink: #1c1c1c;
    --sun: #f6c24a;
    --sun-deep: #f0a43a;
    --coral: #ec8a5c;
    --rainbow-pink: #f3a7b8;
    --rainbow-blue: #8fd0e8;
    --lilac: #b48ee0;
    --logo: #3f4244;
  }
  * { margin: 0; padding: 0; box-sizing: border-box; }
  html, body {
    width: 1200px; height: 1000px; overflow: hidden;
    background: var(--page-bg);
  }
  .canvas { position: relative; width: 1200px; height: 1000px; }

  .flier {
    position: absolute; top: 158px; width: 470px; height: 670px;
    overflow: hidden;
    background:
      radial-gradient(ellipse 60% 40% at 55% 55%, var(--paper-light), transparent 70%),
      linear-gradient(90deg, var(--grunge) 0%, #c9cccc 6%, var(--paper) 16%, var(--paper) 88%, #d3d6d6 100%);
    box-shadow: 8px 10px 14px rgba(0,0,0,0.18);
    color: var(--ink);
    font-family: "Architects Daughter", cursive;
  }
  .flier--front { left: 95px; }
  .flier--back { left: 635px; }

  .flier::before {
    content: ""; position: absolute; left: 0; right: 0; top: 0; height: 60px;
    background: linear-gradient(180deg, rgba(120,124,125,0.55), transparent);
  }

  .artwork {
    position: absolute; border-radius: 40%;
    background:
      radial-gradient(circle at 35% 40%, var(--sun) 0 22%, transparent 23%),
      radial-gradient(circle at 75% 35%, var(--rainbow-pink) 0 14%, transparent 15%),
      radial-gradient(circle at 60% 75%, var(--coral) 0 12%, transparent 13%),
      radial-gradient(ellipse at 50% 50%, rgba(246,194,74,0.35), transparent 70%);
  }
  .front-art-top { left: 205px; top: 0; width: 265px; height: 140px; }
  .front-art-bottom { left: 0; top: 520px; width: 160px; height: 150px; }
  .back-art-top { left: 235px; top: 0; width: 235px; height: 135px; }
  .back-art-bottom-right { left: 330px; top: 460px; width: 140px; height: 210px; }
  .back-art-bottom-left { left: 0; top: 580px; width: 130px; height: 90px; }

  .front-copy { position: absolute; left: 0; right: 0; text-align: center; }
  .presenter { top: 144px; font-size: 15px; letter-spacing: 0.5px; line-height: 22px; padding: 0 70px 0 50px; }
  .event-title { top: 210px; font-size: 27px; line-height: 38px; letter-spacing: 1px; padding: 0 40px; font-weight: 400; }
  .event-date { top: 302px; font-family: "Patrick Hand", cursive; font-size: 21px; }
  .event-date .month { font-family: "Architects Daughter", cursive; font-size: 17px; }
  .event-venue { top: 348px; font-family: "Patrick Hand", cursive; font-size: 19px; line-height: 21px; padding: 0 30px; }
  .event-time { top: 411px; font-family: "Patrick Hand", cursive; font-size: 19px; }
  .event-lineup { top: 500px; font-size: 15px; line-height: 22px; padding: 0 55px; }

  .venue-mark {
    position: absolute; left: 210px; top: 598px;
    display: flex; align-items: center; gap: 10px;
    font-family: "Architects Daughter", cursive;
    font-size: 36px; color: var(--logo); letter-spacing: 2px;
  }
  .venue-mark .mark-dot { width: 14px; height: 14px; border-radius: 50%; background: var(--logo); }

  .back-copy {
    position: absolute; left: 58px; right: 50px;
    font-size: 15.5px; line-height: 23px; text-align: justify;
  }
  .back-intro { top: 116px; }
  .back-guestlist { top: 290px; }
  .back-guestlist .link { word-break: break-all; }
  .back-details {
    position: absolute; left: 40px; right: 40px; top: 462px;
    text-align: center; font-family: "Patrick Hand", cursive; font-size: 19px; line-height: 22px;
  }
</style>
</head>
<body>
<div class="canvas">

  <section class="flier flier--front">
    <div class="artwork front-art-top" role="img" aria-label="Retro sun, swirling clouds and rainbow illustration"></div>
    <div class="artwork front-art-bottom" role="img" aria-label="Star, rainbow arcs and paint splash illustration"></div>

    <p class="front-copy presenter">TRUE PULSE ENTERTAINMENTS PRESENTS A NIGHT CALLED…</p>
    <h1 class="front-copy event-title">‘MIDNIGHT CELLAR RHYTHMZ’</h1>
    <p class="front-copy event-date">Saturday 7th <span class="month">September 2013</span></p>
    <p class="front-copy event-venue">@ Dock47, Harlow Lane, Digbeth, Birmingham B9 3QW</p>
    <p class="front-copy event-time">9pm till late</p>
    <p class="front-copy event-lineup">DJ’s playing a selection of Funky house/deep house/future garage and old school 2-step garage</p>

    <div class="venue-mark"><span>DOCK47</span><span class="mark-dot"></span></div>
  </section>

  <section class="flier flier--back">
    <div class="artwork back-art-top" role="img" aria-label="Retro sun, swirling clouds and rainbow illustration"></div>
    <div class="artwork back-art-bottom-right" role="img" aria-label="Star, rainbow arcs and sparkles illustration"></div>
    <div class="artwork back-art-bottom-left" role="img" aria-label="Sun and swirling cloud illustration"></div>

    <p class="back-copy back-intro">Come and enjoy yourself in a friendly, safe environment with like-minded people who are out to have a good time and rave till the early hours. This venue is part outdoor terrace and part indoor with music being played on the Wavecraft Soundsystem – so you know it is a night not to be missed!!</p>
    <p class="back-copy back-guestlist">This event is guestlist only. Those not on the guest list will not be allowed entry. To get yourself on the guest list go to the sociallink page <span class="link">www.sociallink.example/truepulseentertainments</span> and join the event ‘Midnight Cellar Rhythmz’</p>

    <div class="back-details">
      <p>Dresscode: smart. No<br>trainers/tracksuits</p>
      <p>Admission fee on the door is £5</p>
      <p>Last entry: midnight</p>
    </div>
  </section>

</div>
</body>
</html>
```